Custom Manufacturing Job Shop

We are looking for a business card design for Tall Oak Fabricators Inc. Tall Oak is a family owned business that manufactures any custom product to fit a customers needs, whether it is custom 1 piece or production parts, we truly take on projects that others just cant do. to help in your design go to www.talloakfab.example for a more in depth idea. we have the following capabilities that we would like to see on the card somewhere...maybe on the back of a 2 sided card? we are fully open to ideas.
Machining
• Fabrication
• Millwork
• Maintenance
• Laser Cutting
• Precision Forming
Engineering
Blasting/Painting

No matter how big or small, We literally do it all

preferably black or darker cards but we don't mind to see some color if you see a better fit. we are interested in looking at anything that catches attention.
I have attached our logo, if it is needed in a different file type please let me know and I will send it to you if I can. maybe adding some type of drawing or dimensional lines would be something to add?? just throwing ideas out there....
Updates

Reason: I added one of our shredder designs and would like to see a few more cards if possible using this. any questions please don't hesitate to ask!!

Target Market(s)

anyone looking for design/manufacturing/machining whether it is custom 1 off parts or production.

Industry/Entity Type

Business

Contact Information for Business Card

preferably darker shades, but also not opposed to some color in the same sense....not too bright

Font styles to use
Serif
Sans Serif

Requirements
Must have
• Gus Marrow
• Direct:555-312-7781
• Cell:555-298-4410
• Fax: 555-367-1925
• 42 Quarry Lane
• Dunmoreville, PA 17000
• I also would request having it in a format I can give to the company making the business cards to edit names/numbers etc. for the entire staff.
Nice to have
• drafting lines? we are open to almost anything....
Should not have
• exotic colors

```html
<!DOCTYPE html>
<html lang="en">
<head>
<meta charset="utf-8">
<title>Tall Oak Fabricators – Business Card</title>
<link href="https://fonts.googleapis.com/css2?family=Lato:wght@300;400;700;900&display=swap" rel="stylesheet">
<style>
  :root {
    --backdrop: #d6d6d6;
    --card-white: #ffffff;
    --band-grey: #565656;
    --logo-grey: #4b4b4b;
    --logo-soft: #9a9a9a;
    --text-light: #ffffff;
  }
  * { margin: 0; padding: 0; box-sizing: border-box; }
  html, body {
    width: 1200px;
    height: 926px;
    overflow: hidden;
    background: var(--backdrop);
    font-family: "Lato", sans-serif;
  }
  .card {
    position: absolute;
    left: 120px;
    top: 189px;
    width: 960px;
    height: 549px;
    background: var(--card-white);
    overflow: hidden;
    box-shadow: 0 10px 30px rgba(0,0,0,0.18);
  }
  .card-band {
    position: absolute;
    left: 0;
    top: 0;
    width: 960px;
    height: 549px;
  }
  .card-band path { fill: var(--band-grey); }
  .brand {
    position: absolute;
    left: 0;
    right: 0;
    top: 78px;
    display: flex;
    flex-direction: column;
    align-items: center;
  }
  .brand-row {
    display: flex;
    align-items: center;
    gap: 18px;
  }
  .brand-mark {
    width: 46px;
    height: 46px;
    border-radius: 50%;
    background: var(--logo-soft);
  }
  .brand-name {
    font-weight: 900;
    font-size: 74px;
    letter-spacing: 2px;
    color: var(--logo-grey);
    text-transform: uppercase;
    line-height: 1;
  }
  .brand-web {
    margin-top: 10px;
    font-weight: 400;
    font-size: 24px;
    letter-spacing: 5px;
    color: var(--logo-soft);
    text-transform: uppercase;
  }
  .person {
    position: absolute;
    left: 0;
    right: 0;
    top: 322px;
    text-align: center;
    color: var(--text-light);
    font-size: 40px;
    letter-spacing: 2px;
    text-transform: uppercase;
  }
  .person-first { font-weight: 300; }
  .person-last { font-weight: 700; }
  .contact {
    position: absolute;
    left: 0;
    right: 0;
    color: var(--text-light);
    font-size: 22px;
    letter-spacing: 1.5px;
    text-transform: uppercase;
    text-align: center;
  }
  .contact-phones {
    top: 405px;
    display: flex;
    justify-content: center;
    gap: 44px;
  }
  .contact-address {
    top: 452px;
    font-weight: 700;
    font-size: 24px;
  }
  .contact-label { font-weight: 700; }
</style>
</head>
<body>
  <div class="card">
    <svg class="card-band" viewBox="0 0 960 549" aria-hidden="true">
      <path d="M0,262 C240,248 400,258 458,264 L472,246 L486,266 C640,278 820,300 960,322 L960,549 L0,549 Z"/>
    </svg>

    <div class="brand">
      <div class="brand-row">
        <span class="brand-mark"></span>
        <span class="brand-name">Tall Oak</span>
      </div>
      <div class="brand-web">www.talloakfab.example</div>
    </div>

    <p class="person"><span class="person-first">Gus</span> <span class="person-last">Marrow</span></p>

    <p class="contact contact-phones">
      <span><span class="contact-label">Direct:</span>555-312-7781</span>
      <span><span class="contact-label">Cell:</span>555-298-4410</span>
      <span><span class="contact-label">Fax:</span> 555-367-1925</span>
    </p>
    <p class="contact contact-address">42 Quarry Lane, Dunmoreville, PA 17000</p>
  </div>
</body>
</html>
```